Business Intelligence Application - Reporting Menu and Report Criteria Design

Looking for a fresh, effective and user friendly view for the menu structure and reporting criteria screen format for a business reporting application. Initial format completed, content structure is in place, but we need the 'wow' design.. as its a serious professional report/BI tool it has to fall within certain guidelines for clarity and graphics..but we want it to be slick, friendly, great user experience. There is a large amount of complex content to fit into a small space and we need it to be very inviting, modern and intuitive.. If interested, please review the attachment. We have live screens in operation, but feel these could be improved and looking forward to seeing what great creative suggestions could be made. Please review work done to date in the attached.. We are not looking for a total re-design of everything, all the basic business content/structure is there.. but tell us what we could do to improve this in terms of graphic design... particularly the criteria screens.. thanks!
Updates

Reason: Need a few more days to review designs - thanks for all submissions so far, we will make a selection shortly.

Target Market(s)

Business analysts, hotel operations teams, finance analysts hospitality industry

Industry/Entity Type

Hospitality

Coding

Coded - Design and coding required

Number of Pages Required

4 page

Font styles to use
Sans Serif
Other font styles liked:
• Candara, please see example in deck

Colors
3276b5
3176b5
0255a3
85acd3
33a6d7
cee9f5
85cae6

Requirements
Must have
• sharp clear, logical menu structure, (currently it has 'clicks to sub-menus, we need hover over, slide to sub-menus..) colour, styling.. and most focus on revision of criteria.. right now is somewhat heavy, cumbersome.. keep colour and friendly intuitive process steps.. its heavy analytical stuff.. best of luck!
Should not have
• No grey fonts on white or grey screens! many business apps are not readable or sharp.. or fonts are too small.. colourless, so please avoid that.. see our deck - sharp dark (navy) or black fonts on white, or light shading..

```html
<!DOCTYPE html>
<html lang="en">
<head>
<meta charset="utf-8">
<title>Room Performance – Rollup Criteria</title>
<link href="https://fonts.googleapis.com/css2?family=Open+Sans:wght@400;600&display=swap" rel="stylesheet">
<style>
:root{
  --navy:#0f2340;
  --navy-deep:#0a182c;
  --navy-panel:#14294a;
  --blue:#33a6d7;
  --blue-text:#2a9fd6;
  --ink:#1d2a3a;
  --label:#6b7480;
  --muted:#9aa3ad;
  --line:#e2e6ea;
  --page:#eef2f5;
  --white:#ffffff;
  --cyan:#1cc4d8;
}
*{box-sizing:border-box;margin:0;padding:0}
html,body{width:1200px;height:1193px;overflow:hidden}
body{font-family:"Open Sans",Arial,sans-serif;background:var(--page);color:var(--ink);position:relative}

/* header */
.topbar{position:absolute;left:0;top:0;width:1200px;height:88px;background:var(--white)}
.brand{position:absolute;left:26px;top:25px;display:flex;align-items:center;gap:14px}
.brand-mark{width:38px;height:38px;border-radius:50%;background:var(--cyan)}
.brand-name{font-size:22px;font-weight:400;color:var(--cyan)}
.user{position:absolute;left:721px;top:20px;display:flex;align-items:center;gap:20px}
.avatar{width:46px;height:46px;border-radius:50%;background:linear-gradient(160deg,#b9a18d,#4a3b33)}
.user-name{font-size:14px;color:var(--ink)}
.user-date{font-size:12px;color:var(--muted);margin-top:3px}
.icon-btn{position:absolute;top:21px;width:46px;height:46px;border:1px solid var(--line);border-radius:50%;display:flex;align-items:center;justify-content:center}
.icon-btn.tip{left:1055px}
.icon-btn.settings{left:1127px}

/* main nav */
.mainnav{position:absolute;left:0;top:88px;width:1200px;height:44px;background:var(--navy);display:flex}
.nav-item{width:240px;height:44px;display:flex;align-items:center;padding-left:35px;position:relative;border-right:1px solid #1d3354;color:#c3ccd8;font-size:13px;letter-spacing:1.2px;text-transform:uppercase}
.nav-item.active{background:var(--navy-deep);color:var(--white);font-weight:600}
.nav-icon{width:34px;height:34px;border-radius:50%;background:#23385a;margin-right:13px;display:flex;align-items:center;justify-content:center}
.nav-item.active .nav-icon{background:var(--blue)}
.nav-caret{position:absolute;right:26px;top:17px}
.nav-item.search{border-right:none}

/* page head */
.pagehead{position:absolute;left:0;top:132px;width:1200px;height:142px;background:var(--white)}
.page-title{position:absolute;left:24px;top:38px;font-size:26px;font-weight:400;color:var(--ink)}
.crumbs{position:absolute;right:26px;top:52px;font-size:11.5px;color:var(--muted)}
.crumbs .current{color:var(--blue-text)}
.subtab{position:absolute;left:26px;top:100px;width:185px;height:42px;border-bottom:2px solid var(--blue);font-size:14px;color:var(--blue-text);text-align:center;padding-top:9px}

/* dropdown */
.dropdown{position:absolute;left:240px;top:132px;width:478px;height:192px;display:flex}
.dd-groups{width:239px;background:var(--navy-deep);position:relative;padding-top:22px}
.dd-groups::before{content:"";position:absolute;left:43px;top:18px;width:1px;height:164px;background:#2f4566}
.dd-group{position:relative;height:31px;padding-left:69px;font-size:13px;color:#b5c0cd}
.dd-group::before{content:"";position:absolute;left:43px;top:9px;width:6px;height:1px;background:#3d5579}
.dd-group.current{color:var(--white)}
.dd-group.current::before{width:10px;background:var(--white)}
.dd-links{flex:1;background:var(--navy-panel);position:relative;padding-top:22px}
.dd-links::before{content:"";position:absolute;left:0;top:52px;border-left:8px solid var(--navy-deep);border-top:9px solid transparent;border-bottom:9px solid transparent}
.dd-link{height:31px;padding-left:40px;font-size:13px;color:#b5c0cd}
.dd-link.current{color:var(--blue)}

/* criteria */
.criteria-tabs{position:absolute;left:26px;top:317px;display:flex;gap:3px}
.ctab{width:161px;height:42px;background:linear-gradient(#ffffff,#eef1f4);font-size:13px;color:var(--label);display:flex;align-items:center;justify-content:center}
.ctab.active{background:linear-gradient(#1e3556,#0d1e36);color:var(--white)}
.criteria{position:absolute;left:26px;top:359px;width:1148px;height:781px;background:var(--white)}
.section-bar{height:41px;background:var(--blue);color:var(--white);font-size:13px;letter-spacing:.8px;text-transform:uppercase;padding:0 26px;display:flex;align-items:center;justify-content:space-between}
.section-bar .toggle{font-size:18px;font-weight:400;letter-spacing:0}
.fields{display:grid;grid-template-columns:534px 534px;column-gap:26px;padding:22px 27px 17px}
.field{height:69px}
.field label{display:block;font-size:13px;color:var(--label);height:26px;line-height:18px}
.control{height:33px;border:1px solid var(--line);border-radius:2px;position:relative;font-size:12px;color:var(--muted);padding:0 12px;display:flex;align-items:center}
.control .chev{position:absolute;right:14px;top:13px}
.pair{display:flex;gap:18px}
.pair .control{flex:1}
.control .cal{position:absolute;right:12px;top:10px}
.footer{position:absolute;left:26px;top:1160px;font-size:11px;color:var(--label)}
</style>
</head>
<body>

<header class="topbar">
  <div class="brand"><span class="brand-mark"></span><span class="brand-name">Quillmere Hotels &amp; Resorts</span></div>
  <div class="user">
    <div class="avatar" role="img" aria-label="Portrait photo of the signed-in user"></div>
    <div><div class="user-name">Welcome Daniel Marsh</div><div class="user-date">Oct 03, 2017</div></div>
  </div>
  <div class="icon-btn tip"><svg width="16" height="18" viewBox="0 0 16 18"><circle cx="8" cy="7" r="6" fill="#d5dade"/><rect x="5" y="13" width="6" height="3" rx="1" fill="#d5dade"/></svg></div>
  <div class="icon-btn settings"><svg width="18" height="18" viewBox="0 0 18 18"><circle cx="9" cy="9" r="5.5" fill="none" stroke="#2a9fd6" stroke-width="3" stroke-dasharray="3 1.6"/><circle cx="9" cy="9" r="2" fill="#2a9fd6"/></svg></div>
</header>

<nav class="mainnav">
  <div class="nav-item"><span class="nav-icon"><svg width="12" height="14" viewBox="0 0 12 14"><circle cx="6" cy="4" r="3" fill="#aab5c3"/><path d="M1 13c0-4 10-4 10 0z" fill="#aab5c3"/></svg></span>Admin<svg class="nav-caret" width="9" height="6" viewBox="0 0 9 6"><path d="M1 1l3.5 3.5L8 1" stroke="#8c99aa" fill="none" stroke-width="1.4"/></svg></div>
  <div class="nav-item active"><span class="nav-icon"><svg width="16" height="14" viewBox="0 0 16 14"><rect x="6" y="1" width="4" height="4" fill="#fff"/><rect x="1" y="9" width="4" height="4" fill="#fff"/><rect x="11" y="9" width="4" height="4" fill="#fff"/><path d="M8 5v2M3 9V7h10v2" stroke="#fff" fill="none"/></svg></span>Management<svg class="nav-caret" width="9" height="6" viewBox="0 0 9 6"><path d="M1 1l3.5 3.5L8 1" stroke="#fff" fill="none" stroke-width="1.4"/></svg></div>
  <div class="nav-item"><span class="nav-icon"><svg width="14" height="14" viewBox="0 0 14 14"><circle cx="7" cy="7" r="4.5" fill="none" stroke="#aab5c3" stroke-width="2.4" stroke-dasharray="2.5 1.4"/></svg></span>Intel<svg class="nav-caret" width="9" height="6" viewBox="0 0 9 6"><path d="M1 1l3.5 3.5L8 1" stroke="#8c99aa" fill="none" stroke-width="1.4"/></svg></div>
  <div class="nav-item"><span class="nav-icon"><svg width="14" height="14" viewBox="0 0 14 14"><rect x="1" y="1" width="12" height="8" fill="#aab5c3"/><path d="M7 9v4M4 13h6" stroke="#aab5c3"/></svg></span>Planning<svg class="nav-caret" width="9" height="6" viewBox="0 0 9 6"><path d="M1 1l3.5 3.5L8 1" stroke="#8c99aa" fill="none" stroke-width="1.4"/></svg></div>
  <div class="nav-item search"><span class="nav-icon"><svg width="14" height="14" viewBox="0 0 14 14"><circle cx="8" cy="6" r="4" fill="none" stroke="#aab5c3" stroke-width="1.6"/><path d="M5 9l-3.5 3.5" stroke="#aab5c3" stroke-width="1.8"/></svg></span>Property Search</div>
</nav>

<section class="pagehead">
  <h1 class="page-title">Room Perfomance</h1>
  <div class="crumbs">Management &nbsp;/&nbsp; Consolidations &nbsp;/&nbsp; <span class="current">Rooms Perfomance</span></div>
  <div class="subtab">Revenue Summary</div>
</section>

<div class="criteria-tabs">
  <div class="ctab active">Rollup Criteria</div>
  <div class="ctab">Report Criteria</div>
  <div class="ctab">Edit View</div>
  <div class="ctab">Saved View</div>
  <div class="ctab">Export</div>
</div>

<main class="criteria">
  <div class="section-bar"><span>Geographic / Management Regions</span><span class="toggle">×</span></div>
  <div class="fields">
    <div class="field"><label>Division</label><div class="control"><svg class="chev" width="8" height="5" viewBox="0 0 8 5"><path d="M1 1l3 3 3-3" stroke="#b8bfc7" fill="none"/></svg></div></div>
    <div class="field"><label>My Group</label><div class="control"><svg class="chev" width="8" height="5" viewBox="0 0 8 5"><path d="M1 1l3 3 3-3" stroke="#b8bfc7" fill="none"/></svg></div></div>
    <div class="field"><label>Region</label><div class="control"><svg class="chev" width="8" height="5" viewBox="0 0 8 5"><path d="M1 1l3 3 3-3" stroke="#b8bfc7" fill="none"/></svg></div></div>
    <div class="field"><label>Property Search</label><div class="control"><svg class="chev" width="8" height="5" viewBox="0 0 8 5"><path d="M1 1l3 3 3-3" stroke="#b8bfc7" fill="none"/></svg></div></div>
    <div class="field"><label>Area</label><div class="control"><svg class="chev" width="8" height="5" viewBox="0 0 8 5"><path d="M1 1l3 3 3-3" stroke="#b8bfc7" fill="none"/></svg></div></div>
    <div class="field"><label>Property ID</label><div class="control"><svg class="chev" width="8" height="5" viewBox="0 0 8 5"><path d="M1 1l3 3 3-3" stroke="#b8bfc7" fill="none"/></svg></div></div>
    <div class="field"><label>City</label><div class="control"><svg class="chev" width="8" height="5" viewBox="0 0 8 5"><path d="M1 1l3 3 3-3" stroke="#b8bfc7" fill="none"/></svg></div></div>
    <div class="field"><label>Country Search</label><div class="control"><svg class="chev" width="8" height="5" viewBox="0 0 8 5"><path d="M1 1l3 3 3-3" stroke="#b8bfc7" fill="none"/></svg></div></div>
  </div>

  <div class="section-bar"><span>Operational / BI Filters</span><span class="toggle">×</span></div>
  <div class="fields">
    <div class="field"><label>Brands</label><div class="control"><svg class="chev" width="8" height="5" viewBox="0 0 8 5"><path d="M1 1l3 3 3-3" stroke="#b8bfc7" fill="none"/></svg></div></div>
    <div class="field"><label>Opening Date</label><div class="pair">
      <div class="control"><svg class="cal" width="12" height="11" viewBox="0 0 12 11"><rect x="0.5" y="1.5" width="11" height="9" fill="none" stroke="#b8bfc7"/><path d="M0.5 4h11" stroke="#b8bfc7" stroke-width="2"/></svg></div>
      <div class="control"><svg class="cal" width="12" height="11" viewBox="0 0 12 11"><rect x="0.5" y="1.5" width="11" height="9" fill="none" stroke="#b8bfc7"/><path d="M0.5 4h11" stroke="#b8bfc7" stroke-width="2"/></svg></div>
    </div></div>
    <div class="field"><label>Rating</label><div class="control"><svg class="chev" width="8" height="5" viewBox="0 0 8 5"><path d="M1 1l3 3 3-3" stroke="#b8bfc7" fill="none"/></svg></div></div>
    <div class="field"><label>Room Capacity</label><div class="pair"><div class="control">From: 00</div><div class="control">To: 5000</div></div></div>
    <div class="field"><label>Hotel Type</label><div class="control"><svg class="chev" width="8" height="5" viewBox="0 0 8 5"><path d="M1 1l3 3 3-3" stroke="#b8bfc7" fill="none"/></svg></div></div>
    <div class="field"><label>PMS System</label><div class="control"><svg class="chev" width="8" height="5" viewBox="0 0 8 5"><path d="M1 1l3 3 3-3" stroke="#b8bfc7" fill="none"/></svg></div></div>
    <div class="field"><label>F&amp;B Service</label><div class="control"><svg class="chev" width="8" height="5" viewBox="0 0 8 5"><path d="M1 1l3 3 3-3" stroke="#b8bfc7" fill="none"/></svg></div></div>
    <div class="field"><label>Finance System</label><div class="control"><svg class="chev" width="8" height="5" viewBox="0 0 8 5"><path d="M1 1l3 3 3-3" stroke="#b8bfc7" fill="none"/></svg></div></div>
  </div>

  <div class="section-bar"><span>Currency Conversion</span><span class="toggle">+</span></div>
</main>

<div class="dropdown">
  <div class="dd-groups">
    <div class="dd-group">Summaries</div>
    <div class="dd-group current">Consolidations</div>
    <div class="dd-group">Communication</div>
    <div class="dd-group">Cheat Sheet</div>
    <div class="dd-group">Programs</div>
  </div>
  <div class="dd-links">
    <div class="dd-link">Company Review</div>
    <div class="dd-link current">Room Perfomance</div>
    <div class="dd-link">F&amp;B Perfomance</div>
    <div class="dd-link">Competitive Review</div>
    <div class="dd-link">Operation</div>
  </div>
</div>

<footer class="footer">© 2017 Northbay Analytics. All right reserved.</footer>

</body>
</html>
```